Creative Bright Solar, Geothermal and Wind Website! GO GREEN

We are looking to reface our website. Brightfield energy partners of NY, LLC does Solar, Geothermal and Wind systems. Both on grid and off grid.
Im looking for a fun simple and informative website for customers to sign up for free quotes and see all our systems on a pin point map.
Solar is our main focus and we provide zero down financing with low monthly payments.

Main page should have three buttons to choose solar geo or wind.
"Get a FREE quote" visible and a spot to fill in name, phone, address, email and check boxes for solar geo and wind.

A map of New York that will include all of our systems we have done with a box stating the system size and link to a page with pictures and details of the system.

A meet the team drop down with bios on company employees.

Our current website : bfepofny.com

WE DONT WANT ANYTHING like it. Please. We need simple, fun, up to date, creative an colorful.

Thank you

Target Market(s)

Residential home owners, Commercial and Agricultural

Industry/Entity Type

Solar

Number of Pages Required

2 page

Requirements
Must have
• Map to show all projects completed
• 3 buttons Solar, Geothermal and Wind
• zero down financing
• Low monthly payments
• *** The ability to run the platform Joomla template on the web design.
Nice to have
• I added some pics, please use if you feel fit. your choice.
Should not have
• White background

```html
<!DOCTYPE html>
<html lang="en">
<head>
<meta charset="utf-8">
<title>Brightfield Energy Partners</title>
<link href="https://fonts.googleapis.com/css2?family=Open+Sans:wght@400;600;700&display=swap" rel="stylesheet">
<style>
:root{
  --green:#4f9a2b;
  --orange:#f7941d;
  --orange-light:#f9ab52;
  --ink:#2b2b2b;
  --muted:#666;
  --panel:#ececec;
  --white:#ffffff;
  --footer:#1c1c1c;
  --sky:#6f9cc4;
  --snow:#eef2f5;
}
*{box-sizing:border-box;margin:0;padding:0}
html,body{width:1200px;height:2284px;overflow:hidden}
body{font-family:"Open Sans",Arial,sans-serif;color:var(--ink);background:var(--white);position:relative}
section,header,footer{position:absolute;left:0;width:1200px}

.site-header{top:0;height:120px;background:var(--white)}
.brand{position:absolute;left:120px;top:28px;display:flex;align-items:center;gap:12px}
.brand-dot{width:50px;height:50px;border-radius:50%;background:var(--orange)}
.brand-name{font-size:17px;font-weight:700;color:var(--green);line-height:1.2;width:200px}
.contact-row{position:absolute;right:128px;top:18px;display:flex;align-items:center;gap:10px}
.social{width:22px;height:22px;border-radius:50%;background:#3a7cc9}
.social.alt{background:#46b1e6}
.social.red{background:#d64b3b}
.phone{display:flex;align-items:center;gap:6px;font-size:15px;font-weight:600;color:var(--ink);margin-left:10px}
.main-nav{position:absolute;right:128px;top:66px;display:flex;gap:38px;font-size:12px;font-weight:600;text-transform:uppercase;color:#555}
.main-nav .active{color:var(--green);border-bottom:3px solid var(--green);padding-bottom:6px}

.hero{top:120px;height:510px;background:
  radial-gradient(ellipse 160px 140px at 930px 60px,rgba(255,255,255,.95),rgba(255,255,255,0) 100%),
  radial-gradient(ellipse 120px 190px at 260px 250px,rgba(255,255,255,.85),rgba(255,255,255,0) 100%),
  radial-gradient(ellipse 90px 150px at 470px 290px,rgba(255,255,255,.7),rgba(255,255,255,0) 100%),
  linear-gradient(180deg,#4f82b3 0%,#8fb4d6 32%,#d5e2ec 52%,var(--snow) 64%,#c3d0da 82%,#7f95a6 100%)}
.hero-caption{position:absolute;left:0;right:0;bottom:0;height:78px;background:rgba(255,255,255,.3);display:flex;align-items:center;justify-content:center;font-size:25px;font-weight:600;color:#1d2b36}
.slide-arrow{position:absolute;top:200px;width:48px;height:48px;border-radius:50%;background:rgba(255,255,255,.45)}
.slide-arrow.prev{left:80px}.slide-arrow.next{right:80px}

.welcome{top:630px;height:330px;background:var(--panel)}
.section-title{text-align:center;font-size:27px;font-weight:700;color:var(--ink)}
.section-title::after{content:"";display:block;width:460px;height:2px;background:#bbb;margin:12px auto 0}
.welcome .section-title{padding-top:36px}
.welcome .section-title::after{width:320px}
.welcome-text{position:absolute;left:132px;top:116px;width:580px;font-size:12.5px;line-height:19px;color:var(--muted)}
.welcome-art{position:absolute;left:780px;top:84px;width:300px;height:200px;border-radius:12px;background:
  radial-gradient(ellipse 90px 70px at 130px 100px,#7fb3e0 0%,rgba(127,179,224,0) 100%),
  linear-gradient(90deg,rgba(236,236,236,0) 0%,#dfe6ec 40%,#c9d6e0 100%)}

.systems{top:960px;height:320px;background:var(--orange)}
.system-tile{position:absolute;top:22px;width:210px;height:244px;background:var(--orange-light);display:flex;flex-direction:column;align-items:center;justify-content:center;gap:26px;color:var(--white);font-size:27px;font-weight:600}
.tile-solar{left:232px}.tile-geo{left:480px}.tile-wind{left:728px}

.inquiry{top:1280px;height:320px;background:linear-gradient(160deg,#3a3a3a 0%,#5a5552 50%,#2e2e2e 100%)}
.inquiry-title{text-align:center;color:var(--white);font-size:28px;font-weight:600;padding-top:34px}
.inquiry-title::after{content:"";display:block;width:290px;height:2px;background:rgba(255,255,255,.6);margin:10px auto 0}
.field{position:absolute;height:34px;background:var(--white);font-size:12px;color:#888;padding:8px 10px}
.f-name{left:200px;top:102px;width:250px}
.f-email{left:472px;top:102px;width:250px}
.f-phone{left:744px;top:102px;width:256px}
.f-location{left:200px;top:146px;width:250px}
.f-message{left:472px;top:146px;width:528px;height:68px}
.f-text{left:200px;top:190px;width:250px;display:flex;justify-content:space-between}
.submit{position:absolute;left:527px;top:238px;width:146px;height:36px;background:var(--orange);color:var(--white);font-size:14px;font-weight:700;display:flex;align-items:center;justify-content:center;border-radius:3px}

.benefits{top:1600px;height:140px;background:var(--orange)}
.benefit{position:absolute;top:50px;display:flex;align-items:center;gap:18px;color:var(--white);font-size:21px;font-weight:600}
.benefit-zero{left:200px}.benefit-low{left:610px}
.benefit-divider{position:absolute;left:590px;top:32px;width:2px;height:76px;background:rgba(255,255,255,.55)}

.projects{top:1740px;height:496px;background:var(--panel)}
.projects .section-title{padding-top:36px}
.projects .section-title::after{width:360px}
.project-map{position:absolute;left:72px;top:112px;width:560px;height:360px;background:
  radial-gradient(ellipse 240px 150px at 300px 180px,#f7f8f5 0%,rgba(247,248,245,0) 100%),
  linear-gradient(135deg,#e4e8e0 0%,#f2f3ef 50%,#d9ded5 100%)}
.project-photo{position:absolute;left:672px;top:88px;width:440px;height:240px;background:linear-gradient(180deg,#9cc6ea 0%,#6f9fcf 35%,#2f5f96 60%,#254a78 100%)}
.project-name{position:absolute;left:672px;top:346px;width:440px;font-size:17px;font-weight:700;color:var(--ink)}
.project-text{position:absolute;left:672px;top:374px;width:440px;font-size:12px;line-height:18px;color:var(--muted)}

.site-footer{top:2236px;height:48px;background:var(--footer);color:#ccc;font-size:12px;display:flex;align-items:center;justify-content:space-between;padding:0 120px}
</style>
</head>
<body>

<header class="site-header">
  <div class="brand">
    <span class="brand-dot"></span>
    <span class="brand-name">Brightfield Energy Partners</span>
  </div>
  <div class="contact-row">
    <span class="social"></span>
    <span class="social alt"></span>
    <span class="social red"></span>
    <span class="phone">
      <svg width="16" height="16" viewBox="0 0 24 24"><path d="M6.6 10.8a15 15 0 0 0 6.6 6.6l2.2-2.2c.3-.3.7-.4 1-.2 1.1.4 2.3.6 3.6.6.6 0 1 .4 1 1V20c0 .6-.4 1-1 1A17 17 0 0 1 3 4c0-.6.4-1 1-1h3.5c.6 0 1 .4 1 1 0 1.3.2 2.5.6 3.6.1.3 0 .7-.2 1z" fill="#4f9a2b"/></svg>
      555 014 2290
    </span>
  </div>
  <nav class="main-nav">
    <span class="active">Home</span>
    <span>Solar Power</span>
    <span>Wind Power</span>
    <span>Installations</span>
    <span>Contact Us</span>
  </nav>
</header>

<section class="hero" role="img" aria-label="Geothermal power plant releasing columns of steam over a snowy landscape under a bright blue sky">
  <span class="slide-arrow prev"></span>
  <span class="slide-arrow next"></span>
  <div class="hero-caption">Lorem ipsum dolor sit amet consectetuer adipiscing elit sed</div>
</section>

<section class="welcome">
  <h2 class="section-title">Welcome To Brightfield Energy Partners</h2>
  <p class="welcome-text">We design and install solar, geothermal and wind systems for homes, farms and businesses across New York. Our team handles every step, from the first site visit and system sizing to permits, installation and grid connection. Whether you want to stay on the grid or live fully off it, we build a system that fits your property and your budget. Solar is our main focus, and with zero down financing and low monthly payments, clean power is within reach today. Ask for a free quote and see how much you could save each month.</p>
  <div class="welcome-art" role="img" aria-label="Light bulb lying on its side holding a small landscape with solar panels and wind turbines"></div>
</section>

<section class="systems">
  <div class="system-tile tile-solar">
    <svg width="90" height="70" viewBox="0 0 90 70" fill="none" stroke="#fff" stroke-width="3">
      <path d="M14 8h62l10 40H4z"/><path d="M35 8l-4 40M55 8l4 40M9 28h72"/><path d="M45 48v14M30 64h30"/>
    </svg>
    <span>Solar</span>
  </div>
  <div class="system-tile tile-geo">
    <svg width="90" height="70" viewBox="0 0 90 70" fill="none" stroke="#fff" stroke-width="3">
      <path d="M8 64V38l18-10v10l18-10v10l18-10v36z"/><path d="M70 64V14h10v50"/><path d="M4 64h82"/><path d="M74 10c-4-3 4-5 0-8"/>
      <rect x="18" y="48" width="8" height="8" fill="#fff"/><rect x="36" y="48" width="8" height="8" fill="#fff"/><rect x="54" y="48" width="8" height="8" fill="#fff"/>
    </svg>
    <span>Geothermal</span>
  </div>
  <div class="system-tile tile-wind">
    <svg width="90" height="74" viewBox="0 0 90 74" fill="none" stroke="#fff" stroke-width="3">
      <circle cx="45" cy="26" r="4" fill="#fff"/><path d="M45 22V2M48 28l17 10M42 28L25 38"/><path d="M45 30l-3 42h6z" fill="#fff"/>
    </svg>
    <span>Wind</span>
  </div>
</section>

<section class="inquiry" role="img" aria-label="Darkened photo of a laptop keyboard behind the inquiry form">
  <h2 class="inquiry-title">Quick Inquiry</h2>
  <div class="field f-name">Name</div>
  <div class="field f-email">Email</div>
  <div class="field f-phone">Phone</div>
  <div class="field f-location">Location</div>
  <div class="field f-message">Message</div>
  <div class="field f-text"><span>Text</span><span>&#9662;</span></div>
  <div class="submit">SUBMIT</div>
</section>

<section class="benefits">
  <div class="benefit benefit-zero">
    <svg width="36" height="36" viewBox="0 0 36 36" fill="none" stroke="#fff" stroke-width="3"><rect x="3" y="6" width="26" height="26"/><path d="M10 18l7 7L33 5"/></svg>
    Zero Down Financing
  </div>
  <span class="benefit-divider"></span>
  <div class="benefit benefit-low">
    <svg width="36" height="36" viewBox="0 0 36 36" fill="none" stroke="#fff" stroke-width="3"><rect x="3" y="6" width="26" height="26"/><path d="M10 18l7 7L33 5"/></svg>
    Low Monthly Payments
  </div>
</section>

<section class="projects">
  <h2 class="section-title">Our Completed Projects</h2>
  <div class="project-map" role="img" aria-label="Map of New York State with county outlines and green pins marking each completed installation"></div>
  <div class="project-photo" role="img" aria-label="Installer mounting solar panels on a roof under a blue sky"></div>
  <h3 class="project-name">Lorem ipsum dolor sit amet, consectetuer</h3>
  <p class="project-text">A 9.8 kW rooftop solar array installed on a family home, with panels facing south for strong output through every season of the year.</p>
</section>

<footer class="site-footer">
  <span>Home &nbsp;|&nbsp; Solar Power &nbsp;|&nbsp; Wind Power &nbsp;|&nbsp; Installations &nbsp;|&nbsp; Contact Us</span>
  <span>&copy; 2015 Brightfield Energy Partners &nbsp;|&nbsp; All Rights Reserved.</span>
</footer>

</body>
</html>
```